Centro Renal Lumo Vardeci

Redo a rough draft of the presentation. Some slides are just hand sketches. 15 slides total

Font styles to use
Sans Serif

Colors

Designer to choose colors to be used in the design.

Requirements
Must have
• Use the 'machine' on the dialysis slide. The kidney wherever you feel works to accentuate.
• The slide following the 'supporting cast' should be the same but 'centro Tekali vascular' in bold and maybe the picture vascular acces if works.
• Use the 4 santa Ofelia pictures for 'centro de dialisis santa ofelia' create 4 slides using one picture per slide; go big.
• Create a location slide before the last q&a slide using the location picture
Nice to have
• Please use elegant font for title
• Create something for the estadisticas 2016 slides; not a list like it is now

```html
<!DOCTYPE html>
<html lang="es">
<head>
<meta charset="utf-8">
<title>Centro Renal Lumo Vardeci – Presentación</title>
<link rel="stylesheet" href="https://fonts.googleapis.com/css2?family=Raleway:wght@300;400;600;700&family=Open+Sans:wght@400;600;700&display=swap">
<style>
:root{
  --maroon:#7b2b3d;
  --maroon-dark:#5e1d2c;
  --maroon-soft:#a65a6b;
  --slide:#f1eff0;
  --slide-2:#e3dfe1;
  --ink:#555055;
  --muted:#8a8588;
  --white:#ffffff;
}
*{box-sizing:border-box;margin:0;padding:0}
html,body{width:1200px;height:2340px;overflow:hidden}
body{background:var(--maroon);font-family:"Open Sans",sans-serif;color:var(--ink);position:relative}
.slide{position:absolute;width:570px;height:316px;background:linear-gradient(135deg,var(--slide) 0%,var(--white) 55%,var(--slide-2) 100%);overflow:hidden}
.slide.left{left:20px}.slide.right{left:610px}
.row1{top:660px}.row2{top:996px}.row3{top:1332px}.row4{top:1668px}.row5{top:2004px}
.wave{position:absolute;left:0;bottom:0;width:100%;height:100%;pointer-events:none}
.brand{position:absolute;top:18px;left:22px;display:flex;align-items:center;gap:6px;font-family:"Raleway",sans-serif;font-weight:600;font-size:14px;color:var(--maroon)}
.brand .dot{width:12px;height:12px;border-radius:50%;background:var(--maroon)}
.title{font-family:"Raleway",sans-serif;font-weight:300;color:var(--maroon)}
.cover{left:20px;top:20px;width:1160px;height:620px}
.cover .kidney{position:absolute;left:70px;top:50px;width:300px;height:340px;border-radius:48% 52% 45% 55%/55% 50% 50% 45%;background:radial-gradient(circle at 45% 45%,#f6e9ec,#e2c4cb 70%,#d6b0b9)}
.cover .title{position:absolute;left:450px;top:90px;font-size:84px;line-height:1.08}
.cover .logos{position:absolute;left:0;right:0;top:470px;display:flex;justify-content:center;gap:90px;align-items:center}
.cover .logo{display:flex;align-items:center;gap:10px;font-family:"Raleway",sans-serif;font-weight:600;font-size:30px;color:var(--maroon)}
.cover .logo .mark{width:34px;height:34px;border-radius:50%;background:var(--maroon)}
.cover .logo.small{font-size:16px}
.cover .logo.small .mark{width:30px;height:30px}
.bio .title{position:absolute;left:22px;top:62px;font-size:38px}
.bio ul{position:absolute;left:22px;top:118px;list-style:none;font-size:11px;line-height:1.6;color:var(--muted);width:360px}
.center-title{position:absolute;left:30px;top:110px;font-size:38px;line-height:1.15}
.dialysis{background:var(--white)}
.dialysis .title{position:absolute;left:300px;top:30px;font-size:38px}
.dialysis .machine{position:absolute;left:0;top:60px;width:290px;height:220px;border-radius:0 50% 50% 0;background:linear-gradient(135deg,#c9c3c6,#8e8489 60%,#6e5a62)}
.dialysis .block{position:absolute;left:300px;width:250px;font-size:10.5px;line-height:1.5;color:var(--muted)}
.dialysis .block h4{font-size:13px;color:var(--maroon);font-weight:700;margin-bottom:2px}
.stats .title{position:absolute;left:0;right:0;top:22px;text-align:center;font-size:30px}
.stats .core{position:absolute;left:225px;top:108px;width:120px;height:120px;border-radius:50%;background:var(--maroon)}
.stat{position:absolute;width:130px;font-family:"Raleway",sans-serif}
.stat b{display:block;font-size:32px;font-weight:700;color:var(--maroon)}
.stat span{font-size:10px;color:var(--muted);text-transform:uppercase;letter-spacing:.5px}
.stat.r{text-align:left}.stat.l{text-align:right}
.prov .title{position:absolute;left:22px;top:24px;font-size:34px}
.prov .grid{position:absolute;left:40px;top:90px;width:490px;display:grid;grid-template-columns:repeat(3,1fr);gap:22px 30px}
.badge{height:48px;border-radius:6px;background:#d9d3d6}
.badge:nth-child(odd){background:#c7bdc2}
.cast .title{position:absolute;left:22px;top:20px;font-size:32px}
.node{position:absolute;font-size:11px;font-weight:600;color:var(--maroon);text-align:center;width:120px}
.node .box{width:52px;height:38px;margin:0 auto 4px;border:2px solid var(--maroon);border-radius:6px}
.hub{position:absolute;left:220px;top:150px;width:130px;height:70px;border-radius:8px;background:var(--maroon);color:var(--white);font-size:12px;font-weight:600;display:flex;align-items:center;justify-content:center;text-align:center;padding:8px}
.scene .title{position:absolute;left:22px;top:20px;font-size:32px}
.scene .body{position:absolute;left:22px;top:74px;width:520px;font-size:11px;line-height:1.55;color:var(--muted)}
.scene .body h4{color:var(--maroon);font-size:12.5px;margin-top:8px}
.location .title{position:absolute;left:22px;top:20px;font-size:30px}
.location .map{position:absolute;left:40px;top:80px;width:490px;height:190px;border-radius:6px;background:linear-gradient(135deg,#e5e1e3,#cfc7cb)}
.location .cap{position:absolute;right:40px;bottom:22px;font-size:11px;color:var(--maroon);font-weight:600}
.questions{background:var(--maroon-dark)}
.questions .title{position:absolute;left:0;right:0;top:130px;text-align:center;font-size:42px;color:var(--white)}
</style>
</head>
<body>

<section class="slide cover">
  <svg class="wave" viewBox="0 0 1160 620" preserveAspectRatio="none"><path d="M0 560 C300 500 700 620 1160 540" fill="none" stroke="#d8c3c8" stroke-width="2"/></svg>
  <div class="kidney" role="img" aria-label="Ilustración de un riñón en línea granate"></div>
  <h1 class="title">Centro Renal<br>Lumo Vardeci</h1>
  <div class="logos">
    <div class="logo"><span class="mark"></span>nefrova</div>
    <div class="logo small"><span class="mark"></span>Salud Insular</div>
  </div>
</section>

<section class="slide left row1 bio">
  <div class="brand"><span class="dot"></span>nefrova</div>
  <h2 class="title">Elena Marquet, MD</h2>
  <ul>
    <li>Board Certified in Nephrology</li>
    <li>Medical Director, Centro Renal Lumo Vardeci</li>
    <li>Fellow, Society of Nephrology</li>
    <li>Faculty, School of Medicine</li>
    <li>Member, Kidney Care Council</li>
  </ul>
</section>

<section class="slide right row1 bio">
  <div class="brand"><span class="dot"></span>nefrova</div>
  <h2 class="title">Ing. Tomás J. Olabide</h2>
  <ul>
    <li>B.S. Civil Engineering</li>
    <li>Operations Director, Renal Services Group</li>
    <li>Project Manager, Clinical Facilities</li>
    <li>Centro de Diálisis Santa Ofelia</li>
    <li>Board Member, Health Council</li>
  </ul>
</section>

<section class="slide left row2">
  <svg class="wave" viewBox="0 0 570 316" preserveAspectRatio="none"><path d="M0 260 C160 220 360 320 570 250 L570 316 L0 316Z" fill="#e4dadd"/></svg>
  <h2 class="title center-title">Centro de Diálisis<br>Santa Ofelia</h2>
</section>

<section class="slide right row2 dialysis">
  <div class="machine" role="img" aria-label="Fotografía de una máquina de diálisis"></div>
  <h2 class="title">Dialysis</h2>
  <div class="block" style="top:92px"><h4>Agudo</h4>Tratamiento inmediato para pacientes con falla renal súbita en el hospital.</div>
  <div class="block" style="top:182px"><h4>Crónico</h4>Tratamiento programado de por vida para pacientes con falla renal permanente.</div>
</section>

<section class="slide left row3 stats">
  <h2 class="title">Estadísticas 2016</h2>
  <svg class="wave" viewBox="0 0 570 316"><circle cx="285" cy="168" r="92" fill="none" stroke="#d5c2c7" stroke-width="2"/></svg>
  <div class="core" role="img" aria-label="Riñón blanco sobre círculo granate"></div>
  <div class="stat l" style="left:70px;top:80px"><b>5841</b><span>Tratamientos</span></div>
  <div class="stat l" style="left:70px;top:150px"><b>1140</b><span>Hospitales</span></div>
  <div class="stat l" style="left:70px;top:220px"><b>95</b><span>Pacientes</span></div>
  <div class="stat r" style="left:370px;top:80px"><b>1428</b><span>Referidos</span></div>
  <div class="stat r" style="left:370px;top:150px"><b>66%</b><span>Diabetes</span></div>
  <div class="stat r" style="left:370px;top:220px"><b>20%</b><span>Hipertensión</span></div>
</section>

<section class="slide right row3 prov">
  <h2 class="title">Proveedores</h2>
  <div class="grid">
    <div class="badge"></div><div class="badge"></div><div class="badge"></div>
    <div class="badge"></div><div class="badge"></div><div class="badge"></div>
    <div class="badge"></div>
  </div>
</section>

<section class="slide left row4 cast">
  <h2 class="title">Supporting Cast</h2>
  <svg class="wave" viewBox="0 0 570 316"><g stroke="#7b2b3d" stroke-width="2" fill="none"><path d="M220 170 L150 110"/><path d="M350 170 L420 110"/><path d="M220 205 L150 255"/><path d="M350 205 L420 255"/></g></svg>
  <div class="node" style="left:60px;top:60px"><div class="box"></div>Centro Tekali vascular</div>
  <div class="node" style="left:400px;top:60px"><div class="box"></div>Hospital</div>
  <div class="node" style="left:60px;top:230px"><div class="box"></div>Farmacia</div>
  <div class="node" style="left:400px;top:230px"><div class="box"></div>Transporte</div>
  <div class="hub">Centro de Diálisis Central</div>
</section>

<section class="slide right row4 scene">
  <h2 class="title">Escenario</h2>
  <div class="body">
    <h4>Centro Renal Lumo Vardeci (CRLV)</h4>
    Cuidado renal integral para pacientes en hemodiálisis y diálisis peritoneal, con apoyo de especialistas y educación continua.
    <h4>CISN / Centro Integrado Servicios Nefrova</h4>
    • Nefrología clínica<br>• Acceso vascular<br>• Unidad de diálisis aguda<br>• Educación al paciente
  </div>
</section>

<section class="slide left row5 location">
  <h2 class="title">Valmora Dialysis Centre</h2>
  <div class="map" role="img" aria-label="Mapa de ubicación del centro"></div>
  <div class="cap">Isla Corvana</div>
</section>

<section class="slide right row5 questions">
  <h2 class="title">Questions?</h2>
</section>

</body>
</html>
```